Zelvo RT Biz Card Design

Residential / Commercial/ Emergency

Residential

Tomas Wexley
President
PO Box 4827
Marrow Bay, NY 12873
tomas@zelvo-rt.com
555.555.0187
844.ZELVO.RT
www.zelvo-rt.com
FB: Zelvo RT
Twitter: ZELVO RT

```html
<!DOCTYPE html>
<html lang="en">
<head>
<meta charset="utf-8">
<title>Zelvo RT Business Card</title>
<link rel="stylesheet" href="https://fonts.googleapis.com/css2?family=Oswald:wght@700&family=Arimo:wght@400;700&display=swap">
<style>
  :root {
    --card-black: #0e0e0e;
    --card-black-soft: #1c1c1c;
    --accent-orange: #f5a418;
    --text-white: #f2f2f2;
    --page-bg: #e9e6e1;
    --photo-field: #6e8a4a;
    --photo-house: #3f6b6a;
    --photo-rescue: #8a5a3c;
  }
  * { margin: 0; padding: 0; box-sizing: border-box; }
  html, body { width: 1200px; height: 1000px; overflow: hidden; }
  body {
    background: var(--page-bg);
    font-family: "Arimo", Arial, sans-serif;
    position: relative;
  }
  .card {
    position: absolute;
    left: 190px;
    width: 820px;
    height: 469px;
    background: linear-gradient(135deg, var(--card-black-soft) 0%, var(--card-black) 55%);
    overflow: hidden;
    box-shadow: 0 6px 18px rgba(0,0,0,0.25);
  }
  .card--front { top: 22px; }
  .card--back { top: 509px; }
  .edge-band {
    position: absolute;
    top: 0;
    width: 26px;
    height: 100%;
    background: var(--accent-orange);
  }
  .edge-band--left { left: 0; }
  .edge-band--right { right: 0; }

  .wordmark {
    position: absolute;
    font-family: "Oswald", "Arial Narrow", sans-serif;
    font-weight: 700;
    color: var(--accent-orange);
    letter-spacing: 1px;
    line-height: 1;
    font-size: 92px;
  }
  .rule {
    position: absolute;
    height: 3px;
    background: var(--accent-orange);
  }

  /* front */
  .photo-strip {
    position: absolute;
    top: 24px;
    left: 380px;
    width: 404px;
    height: 150px;
    display: flex;
    gap: 4px;
  }
  .photo { flex: 1; }
  .photo--field { background: linear-gradient(180deg, #9fb3c6 0%, var(--photo-field) 45%, #5a7a36 100%); }
  .photo--house { background: linear-gradient(180deg, #7fa8c8 0%, var(--photo-house) 50%, #2f4f2a 100%); }
  .photo--rescue { background: linear-gradient(180deg, #5c7a3a 0%, var(--photo-rescue) 55%, #b04030 100%); }
  .card--front .wordmark { left: 70px; top: 178px; }
  .card--front .rule { left: 70px; top: 296px; width: 360px; }
  .service-list {
    position: absolute;
    list-style: none;
    color: var(--text-white);
    font-size: 22px;
    line-height: 1.2;
  }
  .service-list--primary { left: 95px; top: 312px; }
  .service-list--secondary { left: 470px; top: 196px; }

  /* back */
  .card--back .wordmark { right: 70px; top: 36px; }
  .card--back .rule { left: 150px; right: 50px; top: 156px; }
  .holder-name {
    position: absolute;
    right: 78px;
    top: 170px;
    font-size: 38px;
    font-weight: 700;
    color: var(--accent-orange);
  }
  .holder-title {
    position: absolute;
    right: 40px;
    top: 228px;
    font-size: 14px;
    color: var(--text-white);
  }
  .contact-list {
    position: absolute;
    left: 60px;
    bottom: 48px;
    list-style: none;
    font-size: 21px;
    line-height: 1.3;
    color: var(--text-white);
  }
  .contact-label { color: var(--accent-orange); font-weight: 700; }
  .address {
    position: absolute;
    right: 60px;
    bottom: 38px;
    font-style: normal;
    text-align: right;
    font-size: 21px;
    line-height: 1.3;
    color: var(--text-white);
  }
  .address .contact-label { display: block; }
</style>
</head>
<body>

<section class="card card--front" aria-label="Card front">
  <div class="edge-band edge-band--left"></div>
  <div class="edge-band edge-band--right"></div>
  <div class="photo-strip">
    <div class="photo photo--field" role="img" aria-label="Photo of a drone spraying a farm field"></div>
    <div class="photo photo--house" role="img" aria-label="Aerial photo of a house by the water"></div>
    <div class="photo photo--rescue" role="img" aria-label="Photo of a search and rescue team member"></div>
  </div>
  <div class="wordmark">ZELVO-RT</div>
  <div class="rule"></div>
  <ul class="service-list service-list--secondary">
    <li>Luxury Yachts</li>
    <li>Post Disaster Views</li>
    <li>Public Safety</li>
    <li>Search &amp; Rescue</li>
    <li>Surveys</li>
  </ul>
  <ul class="service-list service-list--primary">
    <li>Aero Farming</li>
    <li>Cellular Towers</li>
    <li>Comm/Ind Security</li>
    <li>Construction</li>
    <li>Inspections</li>
  </ul>
</section>

<section class="card card--back" aria-label="Card back">
  <div class="edge-band edge-band--left"></div>
  <div class="edge-band edge-band--right"></div>
  <div class="wordmark">ZELVO-RT</div>
  <div class="rule"></div>
  <div class="holder-name">Tomas Wexley</div>
  <div class="holder-title">Owner/President</div>
  <ul class="contact-list">
    <li><span class="contact-label">Domestic USA:</span> 555.555.0187</li>
    <li><span class="contact-label">Toll Free #:</span> 844.ZELVO.RT</li>
    <li><span class="contact-label">Email:</span> tomas@zelvo-rt.com</li>
    <li><span class="contact-label">Web:</span> www.zelvo-rt.com</li>
  </ul>
  <address class="address">
    <span class="contact-label">Address:</span>
    PO Box 4827 Marrow Bay,<br>NY 12873
  </address>
</section>

</body>
</html>
```